Website - TRSC

Having reviewed the designs received so far, no one design is meeting the client’s needs. The client has identified desirable elements from the designs submitted, which we want to see brought together.
Header
It is important that the logo is given space – ie is not overlayed on an image, nor with a short fade into an image. A gradual fade into the header image is acceptable.
Background
While an image background is acceptable, this should only be visible on the left and right borders, it should not be used underneath the main content area.
Main menu
The main menu should be a cohesive bar across the page – not separate buttons. Buttons that are connected together within a bar are acceptable. Menu items should be separated using a pipe ( | ), or by being framed (as long as the framing sits within a bar). Menu item should change colour to indicate the page you are on.
Left Hand Boxes
There should be consistency in colouring through these. It is acceptable to use one colour for the heading , and another for the content area. It is not acceptable for each box to have a different scheme. This applies to the right hand feature boxes as well.
Colouring
We want to keep this simple. Please use colours from the logo, feel free to add complimentary colours but keep the palette limited. If shading is used with any of the colours be careful to not move it too far from the original colour. The yellow does not look good with too much of a grey shade.
Feature Boxes
The two feature boxes on the home page (Browse Homes and Local Knowledge) need to stand out. An option is to ensure that the associated link button uses one of the brighter colours in the palette.
_____________________________________________________
Note: I have attached the newly design logo to the brief. It is important that colours from the logo are used on the design. Blue denotes water and the yellow denotes sand and sun.
I'd like to see the feel of the logo reflected in the site.
______________________________________________
Tui Crib and Seaside Cottages is rebuilding its website – www.tuicribandseasidecottages.co.nz.
We require the design of two pages:
• Home
• House detail page (pgs 3-5 of the attachment).
We have specified a layout for the site (attached).
The contextual information below provides the feeling the site needs to convey.
If further information is required please contact us.
CONTEXT/BACKGROUND
Tui Crib and Seaside Cottages (TRSC) has been in business now for over 11 years and is due for a facelift. We have about 40 – 60 houses available during the peak summer period – about 50% are permanent holiday homes, the balance are local family homes being rented out while they are away on holiday.
We are currently located in Marram Sands – but with the national name have the ability and goal to expand into other areas of New Zealand – so any logo etc has to have the ability to represent other holiday destinations within NZ. Bear in mind that our primary location is Marram at the moment.
Our key market is families going on holiday – looking for a holiday home to book (currently an Marram Sands holiday)
Secondary market is couples or mature groups looking at having some R&R or business groups having some team building/ management meetings away from the busy office surroundings.
We manage ALL the properties so are a great source of information on what holiday home is best suited to each family and “things to do” in the area – i.e. other activities.
Our main focus is to be the best “holiday home” - accommodation provider in whatever location TRSC is representing. We want to be seen as having a good supply of great homes, providing a great service as well as being a good source of local knowledge.
We want to be seen as PROFESSIONALS in the holiday rental business (from occupants and owners).
TRUST – we want people to be able to trust us by listing their property with us (owners) and confidently booking accommodation through us (occupants).
TAGLINE SUGGESTIONS
Key motif – “TRSC, your door to a fine escape!” The “key”, of course is a double play on the house key you get. But it is also extendible to other aspect of the experience we offer. For example the phrase: “getting the key to the city” is applicable to us – we give them the key to Marram…(or whatever location we are marketing in the future). Potentially we may consider promotional merchandise around this, eg promo key rings etc.
Some key words/phrases that our business represents are:
• ‘Our place is your place’
• Connect – connecting families to holiday homes and the area – at the moment only Marram.
• Local – local people looking after your needs – “our place is your place – so make yourself at home!”
• Link – we are the link to a real kiwi holiday experience.
• Holiday - R&R – rest and recreation
More specific to Marram:
• Safe Natural playground – beach, bush, fishing, outdoor activities – creating real family memories.
Website:
• Need to focus on the Local and Personal property management factors in website to differentiate us from other nationwide listing sites – contact us and we can help you find the right accommodation and save you time
• Play on the HOLIDAYMAKER experience more, including giving prominence to visitor deals, become a local etc, differentiating us from other local holiday home rental businesses.
• Real – real people, real places, real experiences.
• User friendly, informative, professional with a personal touch/feel, to encourage the holiday feeling.
Having reviewed the designs received so far, no one design is meetingthe client’s needs. The client has identified desirable elements from thedesigns submitted, which we want to see brought together.
Header
It is important that the logo is given space – ie is not overlayed on animage, nor with a short fade into an image. A gradual fade into the headerimage is acceptable.
Background
While an image background is acceptable, this should only be visible onthe left and right borders, it should not be used underneath the main contentarea.
Main menu
The main menu should be a cohesive bar across the page – not separatebuttons. Buttons that are connected together within a bar are acceptable.Menu items should be separated using a pipe ( | ), or by being framed (as longas the framing sits within a bar). Menu item should change colour to indicatethe page you are on.
Left Hand Boxes
There should be consistency in colouring through these. It isacceptable to use one colour for the heading , and another for the contentarea. It is not acceptable for each box to have a different scheme. Thisapplies to the right hand feature boxes as well.
Colouring
We want to keep this simple. Please use colours from the logo,feel free to add complimentary colours but keep the palette limited. Ifshading is used with any of the colours be careful to not move it too far fromthe original colour. The yellow does not look good with too much of agrey shade.
Feature Boxes
The two feature boxes on the home page (Browse Homes and LocalKnowledge) need to stand out. An option is to ensure that the associated linkbutton uses one of the brighter colours in the palette.

```html
<!DOCTYPE html>
<html lang="en">
<head>
<meta charset="utf-8">
<title>Tui Crib and Seaside Cottages</title>
<link href="https://fonts.googleapis.com/css2?family=PT+Sans+Narrow:wght@400;700&family=Arimo:wght@400;700&display=swap" rel="stylesheet">
<style>
:root{
  --blue:#0a73c8;
  --blue-dark:#0560ad;
  --blue-light:#2c95e6;
  --sky:#1e90ff;
  --yellow:#ffc20e;
  --yellow-light:#ffe15a;
  --orange:#f7a300;
  --cream:#fffdf3;
  --grey-page:#606060;
  --grey-dark:#3c3c3c;
  --text:#333;
  --red:#e8001c;
  --white:#fff;
}
*{box-sizing:border-box;margin:0;padding:0}
html,body{width:1164px;height:1200px;overflow:hidden;background:var(--grey-page)}
body{font-family:"Arimo",Arial,sans-serif;color:var(--text)}
.page{position:absolute;left:0;top:0;width:1144px;height:1179px;transform:scale(1.0175);transform-origin:0 0;background:var(--grey-page)}
.abs{position:absolute}
.scenery{left:0;top:0;width:1144px;height:308px;background:linear-gradient(180deg,#cfe3ee 0%,#4f8a3e 30%,#3f7a36 55%,#9cc4d8 75%,#7fb1cf 100%)}
.logo-panel{left:70px;top:0;width:262px;height:267px;background:linear-gradient(180deg,#fff 0%,#eef5fb 100%);border-left:1px solid #a9cbe4;display:flex;align-items:center;justify-content:center;gap:8px}
.logo-mark{width:18px;height:18px;border-radius:50%;background:var(--yellow);flex:none}
.logo-name{font-family:"PT Sans Narrow",sans-serif;font-size:22px;color:#444;line-height:1.1;width:190px}
.hero{left:332px;top:0;width:708px;height:267px;background:linear-gradient(90deg,#eef5fb 0%,#8ecbee 14%,#3aa3de 45%,#f2d9bf 78%,#e9b48d 100%)}
.hero-title{position:absolute;font-family:Arimo,sans-serif;font-weight:700;color:#1274c8;font-size:28px}
.nav{left:70px;top:267px;width:970px;height:41px;background:linear-gradient(180deg,var(--blue-light),var(--blue-dark));display:flex;align-items:stretch}
.nav a{font-family:"PT Sans Narrow",sans-serif;font-size:19px;color:var(--white);text-decoration:none;display:flex;align-items:center;padding:0 11px;border-right:1px solid #0a5597;box-shadow:1px 0 0 #3c9fe5}
.nav a.current{background:linear-gradient(180deg,var(--yellow-light),var(--yellow));color:#222;margin-top:-9px;padding-top:9px;border-radius:4px 4px 0 0}
.main{left:70px;top:308px;width:970px;height:814px;background:var(--white)}
.box{position:absolute;left:80px;width:262px;border-radius:4px;overflow:hidden}
.box-head{font-family:"PT Sans Narrow",sans-serif;font-weight:700;font-size:24px;padding-left:9px;display:flex;align-items:center}
.quick{top:319px;height:249px;border:1px solid var(--yellow);background:var(--cream)}
.quick .box-head{height:37px;background:linear-gradient(180deg,var(--yellow-light),var(--yellow));color:#222}
.label{position:absolute;font-size:13px;color:#222}
.select{position:absolute;height:27px;border:1px solid #bbb;border-radius:3px;background:linear-gradient(180deg,#fff,#e6e6e6)}
.select::after{content:"";position:absolute;right:5px;top:5px;width:15px;height:15px;background:#fff;border:1px solid #999}
.select::before{content:"";position:absolute;right:9px;top:10px;border:4px solid transparent;border-top:6px solid #222;z-index:1}
.field{position:absolute;height:28px;border:1px solid #bbb;border-radius:3px;background:linear-gradient(180deg,#fff,#e5e5e5);font-size:11px;color:#888;padding:7px 6px}
.btn-dark{position:absolute;background:linear-gradient(180deg,#6a6a6a,#2e2e2e);color:#fff;font-weight:700;font-size:15px;display:flex;align-items:center;justify-content:center;border-radius:3px}
.touch{top:588px;height:217px;border:1px solid var(--blue)}
.touch .box-head,.deals .box-head{height:38px;color:#fff}
.touch .box-head{background:linear-gradient(180deg,var(--blue-light),var(--blue-dark))}
.deals{top:828px;height:217px;border:1px solid #555;background:#f3f3f3}
.deals .box-head{background:linear-gradient(180deg,#777,#333)}
.deal-photo{position:absolute;left:6px;top:44px;width:118px;height:128px;background:linear-gradient(180deg,#bfe2f5,#f0f6f9 60%,#d9c3ae)}
.deal-text{position:absolute;left:134px;top:40px;width:124px;font-size:13.5px;line-height:22px;color:#222}
.share{left:80px;top:1058px;width:262px;height:52px;border:1px solid #9cc1e0;background:#eef5fb;display:flex;align-items:center;padding-left:4px;gap:20px}
.sq{width:34px;height:34px;border-radius:4px}
.title{left:363px;top:323px;font-family:"PT Sans Narrow",sans-serif;font-size:24px;color:var(--blue)}
.para{position:absolute;font-size:12.6px;line-height:16.8px;color:#333;text-align:justify}
.shortlist{left:879px;top:325px;width:139px;height:85px;border:1px solid #e08b00;border-radius:3px;background:linear-gradient(180deg,var(--yellow-light),var(--orange));color:#fff;font-weight:700;font-size:28px;line-height:30px;text-align:center;padding-top:10px;text-shadow:0 1px 2px #7a5200}
.help{left:879px;top:421px;width:139px;height:205px;border:1px solid #b8d6ee;border-radius:3px;background:linear-gradient(180deg,#e5f2fc,#fff);text-align:center}
.help h3{font-size:27px;color:var(--sky);margin-top:6px}
.help p{font-size:15px;font-weight:700;line-height:21px;color:#333;letter-spacing:.3px;margin-top:2px}
.help .phone{color:var(--red);font-size:16px;margin-top:6px;letter-spacing:0}
.cta{left:363px;top:786px;width:655px;text-align:center;font-weight:700;font-size:24px;line-height:33px;color:#333}
.cta span{color:var(--sky)}
.feature{position:absolute;top:871px;height:239px;border-radius:4px;overflow:hidden;box-shadow:0 2px 4px rgba(0,0,0,.35)}
.feature .photo{height:199px}
.feature .link{height:40px;color:#fff;font-weight:700;font-size:17px;display:flex;align-items:center;justify-content:center}
.f-browse{left:363px;width:331px;border:1px solid var(--sky)}
.f-browse .photo{background:linear-gradient(180deg,#5d8fc8 0%,#c79a5a 45%,#8a4a1c 70%,#3d8fb0 100%)}
.f-browse .link{background:var(--sky)}
.f-local{left:714px;width:303px;border:1px solid var(--yellow)}
.f-local .photo{background:linear-gradient(180deg,#8fc4ea 0%,#4f8c3c 35%,#c9b48a 55%,#2eb6d6 80%,#30a8cf 100%)}
.f-local .link{background:var(--yellow)}
.footer{left:0;top:1122px;width:1144px;height:57px;background:var(--blue);display:flex;justify-content:center;align-items:center;gap:16px;padding-left:10px}
.footer a{color:#fff;font-size:14px;text-decoration:none}
</style>
</head>
<body>
<div class="page">
  <div class="abs scenery" role="img" aria-label="Coastal scenery with bush-clad hills and a moored yacht"></div>

  <header>
    <div class="abs logo-panel"><span class="logo-mark"></span><span class="logo-name">Tui Crib &amp; Seaside Cottages</span></div>
    <div class="abs hero" role="img" aria-label="Sunny harbour town and a smiling family relaxing on a sun lounger">
      <span class="hero-title" style="left:162px;top:46px">Lorem Ipsum Dlor Sit</span>
      <span class="hero-title" style="left:294px;top:80px">Ipsum Dlor Sit</span>
    </div>
    <nav class="abs nav">
      <a href="#">Home</a>
      <a href="#">Browse Homes</a>
      <a href="#">Packages</a>
      <a href="#" class="current" style="margin-left:8px">Local Knowledge</a>
      <a href="#">About us</a>
      <a href="#">Contact us</a>
      <a href="#">List your Homes</a>
    </nav>
  </header>

  <main class="abs main"></main>

  <section class="box quick">
    <div class="box-head">Quick Search</div>
    <span class="label" style="left:9px;top:45px">No. Of Guests Beach</span>
    <div class="select" style="left:8px;top:64px;width:245px"></div>
    <span class="label" style="left:9px;top:104px">Nightly Rate</span>
    <div class="select" style="left:8px;top:124px;width:116px"></div>
    <span class="label" style="left:134px;top:131px">to</span>
    <div class="select" style="left:158px;top:124px;width:95px"></div>
    <span class="label" style="left:9px;top:166px">Keyword</span>
    <div class="field" style="left:8px;top:186px;width:210px">Beach Access</div>
    <div class="btn-dark" style="left:211px;top:186px;width:42px;height:28px">GO</div>
    <span class="label" style="left:9px;top:228px;font-size:12px;color:var(--blue)">Advanced Search</span>
  </section>

  <section class="box touch">
    <div class="box-head">Keep In Touch</div>
    <p style="position:absolute;left:0;top:42px;width:262px;text-align:center;font-size:15.5px;line-height:22px;color:#444">Newsletter with Deals &amp;<br>Local Knowledge To Your Inbox</p>
    <span class="label" style="left:7px;top:98px;font-size:16px">Name</span>
    <div class="field" style="left:56px;top:91px;width:198px"></div>
    <span class="label" style="left:7px;top:140px;font-size:16px">Email</span>
    <div class="field" style="left:56px;top:133px;width:198px"></div>
    <div style="position:absolute;left:8px;top:175px;width:104px;height:30px;border-radius:3px;background:linear-gradient(180deg,#4a78c9,#2b57a3);color:#fff;font-size:13.5px;padding:7px 6px">Follow Us</div>
    <div class="btn-dark" style="left:201px;top:175px;width:53px;height:30px">GO</div>
  </section>

  <section class="box deals">
    <div class="box-head">Deals</div>
    <div class="deal-photo" role="img" aria-label="Couple relaxing on a white sun lounger"></div>
    <p class="deal-text">Lorem ipsum Lorem ipsum dolor sit &nbsp;Lorem ipsum Lorem ipsum dolor sit Lorem Lorem ipsum</p>
    <span class="label" style="left:17px;top:189px;font-weight:700;font-size:14px;color:var(--blue)">VIEW</span>
    <div class="btn-dark" style="left:201px;top:181px;width:53px;height:28px">View</div>
  </section>

  <section class="abs share">
    <svg width="40" height="38" viewBox="0 0 40 38"><rect x="2" y="8" width="36" height="26" fill="#f4f4f4" stroke="#777" stroke-width="1.5"/><path d="M2 8 L20 23 L38 8" fill="none" stroke="#777" stroke-width="1.5"/></svg>
    <span class="sq" style="background:#5bc3f0"></span>
    <span class="sq" style="background:#3b5b98;width:32px"></span>
    <span style="font-size:14px;color:#222">Share This</span>
  </section>

  <h1 class="abs title">Welcome to Tui Crib &amp; Seaside Cottages</h1>
  <p class="para" style="left:363px;top:363px;width:484px">Lorem ipsum onsectetuer adipiscing elit, sed diam nonummy nibh euismod tincidunt ut laoreet dolore magna aliquam erat volutpat. Ut wisi enim ad minim veniam, quis nostrud exerci tation ullamcorper suscipit lobortis nisl ut aliquip ex ea commodo consequat.</p>
  <p class="para" style="left:363px;top:447px;width:484px">Lorem ipsum onsectetuer adipiscing elit, sed diam nonummy nibh euismod tincidunt ut laoreet dolore magna aliquam erat volutpat. Ut wisi enim ad minim veniam, quis nostrud exerci tation ullamcorper suscipit lobortis nisl ut aliquip ex ea commodo consequat.</p>
  <p class="para" style="left:363px;top:531px;width:484px">Lorem ipsum onsectetuer adipiscing elit, sed diam nonummy nibh euismod tincidunt ut laoreet dolore magna aliquam erat volutpat. Ut wisi enim ad minim veniam, quis nostrud exerci tation ullamcorper suscipit lobortis nisl ut aliquip ex ea commodo consequat.</p>

  <div class="abs shortlist">My<br>Shortlist</div>
  <aside class="abs help">
    <h3>Help !</h3>
    <p>Can't Find What You're Looking For?<br>Contact Us For A Personal Property Search</p>
    <p class="phone">+64-21-555-0182</p>
  </aside>

  <p class="para" style="left:364px;top:641px;width:651px">Lorem ipsum onsectetuer adipiscing elit, sed diam nonummy nibh euismod tincidunt ut laoreet dolore magna aliquam erat volutpat. Ut wisi enim ad minim veniam, quis nostrud exerci tation ullamcorper suscipit lobortis nisl ut aliquip ex ea commodo consequat.</p>
  <p class="para" style="left:364px;top:717px;width:651px">Lorem ipsum onsectetuer adipiscing elit, sed diam nonummy nibh euismod tincidunt ut laoreet dolore magna aliquam erat volutpat. Ut wisi enim ad minim veniam, quis nostrud exerci tation ullamcorper suscipit lobortis nisl ut aliquip ex ea commodo consequat.</p>

  <p class="abs cta">Just can't find what you're looking for?<br><span>Contact us</span> for a personal property search.</p>

  <a class="feature f-browse" href="#" style="text-decoration:none">
    <div class="photo" role="img" aria-label="Grand holiday villa lit up at dusk beside a pool"></div>
    <div class="link">Browse Homes</div>
  </a>
  <a class="feature f-local" href="#" style="text-decoration:none">
    <div class="photo" role="img" aria-label="Resort lagoon pool among palm trees and thatched huts"></div>
    <div class="link">Local Knowledge</div>
  </a>

  <footer class="abs footer">
    <a href="#">Terms &amp; Conditions</a>
    <a href="#">Privacy Policy</a>
    <a href="#">Contact Us List</a>
    <a href="#">Your Home</a>
  </footer>
</div>
</body>
</html>
```